Brell Harbor Company Business Cards

Front and Back Business Card - logo and text setup - cool design. I need workable photoshop or illustrator files so I can setup each employee card with design that is created
Updates

Hi everyone, thank you for the great entries. Please no more white and blue cards - there are so many already - black and silver only now please. thanks!

Target Market(s)

Construction Industry - Facility Managers

Industry/Entity Type

Construction

Contact Information for Business Card

I really like contemporary simplistic looks - clean neat....not opposed to seeing some black backrounds

Requirements
Must have
• Logo/website address with design on front only - www.brellharbor-example.com (logo attached)
• Back:
• Name/Title/Company Address/Phone/email address
Nice to have
• Cool design
Should not have
• Nothing gimmicky like Fire or Water - since we are a Fire Protection company - it has all been done

```html
<!DOCTYPE html>
<html lang="en">
<head>
<meta charset="utf-8">
<title>Brell Harbor Company – Business Cards</title>
<link rel="stylesheet" href="https://fonts.googleapis.com/css2?family=Montserrat:wght@300;400;700;800&display=swap">
<style>
  :root {
    --backdrop: #d1d2d4;
    --card-front: #ffffff;
    --card-back: #4a4a4c;
    --brand-grey: #c9c9cb;
    --text-light: #f2f2f2;
    --text-soft: #e6e6e6;
    --radius: 32px;
  }
  * { margin: 0; padding: 0; box-sizing: border-box; }
  html, body {
    width: 1200px; height: 1200px; overflow: hidden;
    background: var(--backdrop);
    font-family: "Montserrat", sans-serif;
  }
  .canvas { position: relative; width: 1200px; height: 1200px; }

  .card {
    position: absolute; left: 181px; width: 840px; height: 478px;
    border-radius: var(--radius); overflow: hidden;
  }
  .card-texture { position: absolute; inset: 0; }

  /* Front */
  .card--front { top: 96px; background: var(--card-front); }
  .card--front .card-texture { background: var(--card-front); }
  .brand-bar {
    position: absolute; left: 0; top: 375px;
    width: 387px; height: 11px; background: var(--brand-grey);
  }
  .brand-name {
    position: absolute; right: 62px; top: 303px;
    font-weight: 800; font-size: 54px; line-height: 1;
    letter-spacing: -1px; color: var(--brand-grey);
  }

  /* Back */
  .card--back { top: 634px; background: var(--card-back); }
  .card--back .card-texture { background: var(--card-back); }
  .holder {
    position: absolute; left: 0; right: 0; top: 146px; text-align: center;
  }
  .holder-name {
    font-weight: 700; font-size: 56px; line-height: 1;
    letter-spacing: 1.5px; color: var(--text-light);
  }
  .holder-title {
    margin-top: 14px;
    font-weight: 300; font-size: 28px; line-height: 1;
    color: var(--text-soft);
  }
  .contact {
    position: absolute; top: 345px;
    display: flex; align-items: flex-start; gap: 12px;
    font-weight: 400; font-size: 17px; line-height: 24px;
    color: var(--text-soft);
  }
  .contact svg { flex: none; margin-top: 2px; fill: var(--text-soft); }
  .contact--phone { left: 52px; }
  .contact--address { left: 256px; }
  .contact--web { left: 508px; }
</style>
</head>
<body>
<div class="canvas">

  <section class="card card--front" aria-label="Business card front">
    <div class="card-texture" role="img" aria-label="Faint diamond lattice texture across the card"></div>
    <div class="brand-bar"></div>
    <div class="brand-name">Brell Harbor</div>
  </section>

  <section class="card card--back" aria-label="Business card back">
    <div class="card-texture" role="img" aria-label="Faint diamond lattice texture across the card"></div>

    <div class="holder">
      <h1 class="holder-name">MARCUS DALE</h1>
      <p class="holder-title">Facility Manager</p>
    </div>

    <div class="contact contact--phone">
      <svg width="22" height="22" viewBox="0 0 24 24" aria-hidden="true">
        <path d="M6.6 10.8a15.2 15.2 0 0 0 6.6 6.6l2.2-2.2a1 1 0 0 1 1-.25 11.4 11.4 0 0 0 3.6.57 1 1 0 0 1 1 1V20a1 1 0 0 1-1 1A17 17 0 0 1 3 4a1 1 0 0 1 1-1h3.5a1 1 0 0 1 1 1c0 1.25.2 2.45.57 3.57a1 1 0 0 1-.25 1z"/>
      </svg>
      <p>015 555 0142<br>012 555 0178</p>
    </div>

    <div class="contact contact--address">
      <svg width="18" height="24" viewBox="0 0 18 24" aria-hidden="true">
        <path d="M9 0a8 8 0 0 0-8 8c0 6 8 15 8 15s8-9 8-15a8 8 0 0 0-8-8zm0 11a3 3 0 1 1 0-6 3 3 0 0 1 0 6z"/>
      </svg>
      <p>#512 Corran Vale Rd,<br>Ostley VA 1830VA</p>
    </div>

    <div class="contact contact--web">
      <svg width="26" height="20" viewBox="0 0 26 20" aria-hidden="true">
        <path d="M1 2h24v16H1z M2.5 3.5 13 11l10.5-7.5" fill="none" stroke="#e6e6e6" stroke-width="2"/>
        <path d="M2 17l8-7M24 17l-8-7" stroke="#e6e6e6" stroke-width="2"/>
      </svg>
      <p>info@brellharbor-example.com<br>www.brellharbor-example.com</p>
    </div>
  </section>

</div>
</body>
</html>
```